Cinco de Mayo Event Poster- Los Cerritos

I need a poster for our restaurant, Los Cerritos, for Cinco de Mayo.
Final Size 11"x17"(portrait).
Use our official Los Cerritos Logo.
Date: Tuesday May 5
Live Music/ Mariachi/ DJ/ Ice Luge/ Beer Tent/ Giveaways.
Include our phone number 555-418-2936
Address : 47116 Garnet Rd, Livonia, MI 48150
website : www.loscerritoskitchen-demo.com

Industry/Entity Type

Restaurant

Colors
0054AA
0677BA
7BADD7
CADEEF
E8F1F8
0094D4
00A9DD
6FCCEA
C7EBF8
E9F6FB
00AB8E
00BBA5
67D7C9
C6EFE9
E9F9F6
FFC000
F8CF3A
FAE287
FDF2CF
FEFAEE
EE7325
F08F49
F5BC92
FAE3D3
FDF4ED
E54698
E96AAD
F1A4CE
F9D9EA
FCEFF6
A7469A
B969AE
D3A5CF
EDDBEB
F8F0F9
6B429C
8869AF
B7A5CE
E3DAEB
F3F0F8

Requirements
Must have
• Vereda Tequila Logo, Lumbral Tequila Logo.
Nice to have
• Palm Trees, margaritas, Mexican beer. I added our menus to give you a better Idea of who we are.vd
Should not have
• maracas/sombreros

```html
<!DOCTYPE html>
<html lang="en">
<head>
<meta charset="utf-8">
<title>Los Cerritos – Cinco de Mayo Poster</title>
<link rel="stylesheet" href="https://fonts.googleapis.com/css2?family=Lato:wght@700;900&family=Rye&display=swap">
<style>
  :root {
    --pink: #d93a7b;
    --pink-deep: #d6418a;
    --orange: #ec8e1a;
    --teal: #00bba5;
    --blue: #2f62ad;
    --navy: #111e36;
    --purple: #7b22b0;
    --black: #050505;
    --cream: #eef6f2;
    --gold: #f7b21a;
    --lime: #c8e24a;
    --ink: #1a1a1a;
    --drink-red: #7a3418;
    --palm-green: #4f8f2f;
    --margarita: #d8e37a;
  }
  html, body {
    margin: 0;
    width: 1200px;
    height: 1200px;
    overflow: hidden;
    background: #ffffff;
  }
  .poster-canvas { display: block; width: 1200px; height: 1200px; }
  .brand-name { font-family: "Lato", sans-serif; font-weight: 900; fill: var(--orange); }
  .title-cinco { font-family: "Rye", serif; fill: var(--cream); stroke: var(--ink); stroke-width: 4; paint-order: stroke; }
  .title-de { font-family: "Rye", serif; fill: var(--gold); stroke: var(--ink); stroke-width: 4; paint-order: stroke; }
  .title-mayo { font-family: "Rye", serif; fill: var(--pink-deep); stroke: var(--ink); stroke-width: 4; paint-order: stroke; }
  .feature-music { font-family: "Lato", sans-serif; font-weight: 900; fill: var(--orange); }
  .feature-extras { font-family: "Lato", sans-serif; font-weight: 900; fill: var(--lime); }
  .event-day { font-family: "Lato", sans-serif; font-weight: 900; fill: var(--cream); }
  .event-info { font-family: "Lato", sans-serif; font-weight: 700; fill: var(--cream); }
  .sponsor-name { font-family: "Lato", sans-serif; font-weight: 900; fill: #ffffff; }
</style>
</head>
<body>
<svg class="poster-canvas" viewBox="0 0 1932 1932" xmlns="http://www.w3.org/2000/svg">
  <g class="poster-background">
    <rect x="360" y="36" width="1212" height="1864" fill="var(--pink)"/>
    <polygon points="360,240 760,320 960,900 360,960" fill="var(--orange)"/>
    <polygon points="760,320 1040,320 1130,700 960,900" fill="var(--teal)"/>
    <polygon points="1264,36 1572,36 1572,520 1130,700 1040,320 1264,320" fill="var(--blue)"/>
    <polygon points="1130,700 1572,480 1572,860 1000,1240 960,900" fill="var(--navy)"/>
    <polygon points="360,960 960,900 1000,1240 1040,1590 360,1130" fill="var(--purple)"/>
    <polygon points="360,1130 470,970 980,1060 1040,1590 360,1600" fill="var(--black)"/>
    <polygon points="1000,1240 1572,860 1572,1190 1040,1590" fill="var(--orange)"/>
    <polygon points="1030,1030 1572,700 1572,860 1180,1215" fill="var(--navy)"/>
    <polygon points="840,1110 1000,1000 1120,1250 990,1330" fill="var(--purple)"/>
    <polygon points="1040,1590 1572,1190 1572,1900 1180,1900" fill="var(--purple)"/>
    <polygon points="360,1600 1040,1590 1180,1900 360,1900" fill="var(--pink)"/>
  </g>

  <g class="brand-header">
    <circle cx="718" cy="200" r="52" fill="var(--gold)"/>
    <text class="brand-name" x="800" y="232" font-size="104">Los Cerritos</text>
  </g>

  <g class="event-title">
    <text class="title-cinco" x="455" y="560" font-size="250" textLength="740" lengthAdjust="spacingAndGlyphs">CINCO</text>
    <text class="title-de" x="598" y="712" font-size="130">DE</text>
    <text class="title-mayo" x="790" y="750" font-size="240" textLength="690" lengthAdjust="spacingAndGlyphs">MAYO</text>
  </g>

  <rect class="illustration-michelada" role="img" aria-label="Illustration of a michelada with salted rim, beer bottle pouring, lime and chili peppers" x="400" y="760" width="350" height="300" rx="30" fill="var(--drink-red)"/>

  <g class="feature-list-music">
    <text class="feature-music" font-size="82" transform="translate(440 1310) rotate(-27)">LIVE MUSIC</text>
    <text class="feature-music" font-size="82" transform="translate(548 1370) rotate(-27)">MARIACHI</text>
    <text class="feature-music" font-size="82" transform="translate(962 1304) rotate(-27)">DJ</text>
  </g>

  <g class="feature-list-extras">
    <text class="feature-extras" font-size="62" transform="translate(1100 1095) rotate(-40)">ICE LUGE</text>
    <text class="feature-extras" font-size="62" transform="translate(1150 1145) rotate(-40)">BEER TENT</text>
    <text class="feature-extras" font-size="62" transform="translate(1205 1195) rotate(-40)">GIVEAWAYS</text>
  </g>

  <rect class="illustration-palm" role="img" aria-label="Illustration of a palm tree" x="1260" y="1160" width="240" height="330" rx="40" fill="var(--palm-green)"/>
  <rect class="illustration-margaritas" role="img" aria-label="Illustration of a lime margarita and a strawberry margarita toasting" x="750" y="1370" width="460" height="310" rx="40" fill="var(--margarita)"/>

  <g class="event-details">
    <text class="event-day" x="415" y="1563" font-size="68">TUESDAY</text>
    <text class="event-day" x="413" y="1660" font-size="102">MAY 5</text>
    <text class="event-info" x="415" y="1760" font-size="44">Garnet Rd, Livonia, MI 48150</text>
    <text class="event-info" x="415" y="1832" font-size="46">555-418-2936</text>
    <text class="event-info" x="415" y="1889" font-size="38">www.loscerritoskitchen-demo.com</text>
  </g>

  <g class="sponsors">
    <text class="sponsor-name" x="1425" y="1568" font-size="48" text-anchor="middle">Vereda</text>
    <text class="sponsor-name" x="1425" y="1690" font-size="44" text-anchor="middle">Lumbral</text>
    <circle cx="1425" cy="1790" r="48" fill="#ffffff"/>
  </g>
</svg>
</body>
</html>
```